Car Club Website- Kestrel Roadster Club of New Zealand

We have been running a website in NZ for Kestrel Roadster Car enthusiasts. The design was fairly basic and is in serious need of a revamp, http://garagepalisade.example.org/index.html. We are looking for a dynamic design that will be visually attractive ( and obvious ) to our visitors and incorporates the fundamentals of the previous website. The inmportant tabs are the forum, gallery and events and the website needs to be easy to use for everyone.

This is all about the cars and the people. Visually, you need to recognise that we are a NZ Car Club and as such we do not want graphics of Left Hand Drive Cars or anything obviously NOT from NZ.
Thanks, cheers Wes

I AM VERY INTERESTED TO SEE SOMETHING THAT IS TOTALLY DIFFERENT TO ANYTHING YET POSTED. THE DESIGNS WE HAVE ARE GOOD AND I WILL PICK ONE OF THOSE BUT REALLY WANT TO SEE SOMETHING CREATIVE AND EYE CATCHING. I HAVE NOW CHANGED TO NON REFUNDABLE SO SOMEONE WILL GET PAID.
Updates

HI All, thanks for input so far but I have not seen a really creative left field approach yet which I am looking for. Thanks, cheers Wes

Target Market(s)

Car Enthusiasts

Industry/Entity Type

Events

Requirements
Must have
• as per link website
Should not have
• Any obvious graphics not from NZ

```html
<!DOCTYPE html>
<html lang="en">
<head>
<meta charset="utf-8">
<title>Kestrel Club of New Zealand</title>
<link href="https://fonts.googleapis.com/css2?family=Oswald:wght@400;500&family=Open+Sans:wght@400;600&display=swap" rel="stylesheet">
<style>
  :root{
    --navy:#1f2d5c;
    --nav-top:#34477e;
    --nav-bottom:#1c2b58;
    --text:#2b2b2b;
    --red:#d0202a;
    --heading-bg:#e9e9ea;
    --page-bg:#dcdcdd;
    --panel:#ffffff;
    --caption:rgba(0,0,0,.6);
    --link-muted:#c9c9c9;
  }
  *{box-sizing:border-box;margin:0;padding:0}
  html,body{width:948px;height:1200px;overflow:hidden}
  body{background:var(--page-bg);font-family:"Open Sans",Arial,sans-serif;color:var(--text);position:relative}
  .page{position:absolute;left:136px;top:0;width:676px;height:1200px;background:var(--panel);box-shadow:0 0 10px rgba(0,0,0,.25)}
  .abs{position:absolute}
  .photo{position:absolute;overflow:hidden}
  .caption{position:absolute;left:0;right:0;bottom:0;height:34px;background:var(--caption);color:#fff;font-size:11.5px;padding:9px 13px;font-weight:400}
  .caption span{color:var(--link-muted)}
  .brand-photo{left:8px;top:9px;width:174px;height:116px;border-radius:6px;background:radial-gradient(ellipse at 50% 55%,#5a6fb5 0%,#2c3f86 45%,#1a1f35 80%,#ffffff 81%)}
  .brand-name{left:194px;top:18px;color:var(--navy);font-family:"Oswald",sans-serif;font-weight:500;line-height:1}
  .brand-name .main{font-size:44px;letter-spacing:-.5px;display:block}
  .brand-name .sub{font-size:20px;display:block;margin-top:4px;letter-spacing:.5px}
  .ad-note{left:456px;top:34px;width:220px;font-size:10px;line-height:15px;color:var(--red);text-transform:uppercase}
  .ad-box{left:456px;top:70px;width:211px;height:24px;background:#9a9a9a;color:#fff;font-family:"Open Sans",sans-serif;font-weight:600;font-size:14px;line-height:24px;padding-left:8px}
  .nav{left:7px;top:136px;width:661px;background:linear-gradient(var(--nav-top),var(--nav-bottom));display:flex;border-bottom:4px solid #c9ccd6;height:39px}
  .nav a{display:block;height:35px;line-height:35px;text-align:center;color:#fff;text-decoration:none;font-family:"Oswald",sans-serif;font-size:13.5px;border-right:1px solid #142048;box-shadow:1px 0 0 #4a5b8e}
  .h-title{font-family:"Oswald",sans-serif;font-weight:400;color:var(--navy);font-size:16px;letter-spacing:-.3px;line-height:1;white-space:nowrap}
  .h-box{position:absolute;background:var(--heading-bg);border-top:2px solid #dcdcdc;height:33px;padding:6px 10px;font-family:"Oswald",sans-serif;color:var(--navy);font-size:17px;line-height:1.1;white-space:nowrap}
  .copy{position:absolute;font-size:9.6px;line-height:14.4px}
  .copy p+p{margin-top:14.4px}
  .rule{left:7px;top:1071px;width:661px;height:1px;background:#d0d0d0}
  .disclaimer{left:0;top:1087px;width:676px;text-align:center;font-size:8.3px;color:var(--red)}
  .sponsor-note{left:0;top:1117px;width:676px;text-align:center;font-size:8.5px;color:#222}
  .sponsor{left:291px;top:1135px;width:94px;height:40px;background:#111;color:#e8a23a;font-family:"Oswald",sans-serif;font-size:11px;display:flex;align-items:center;justify-content:center}
</style>
</head>
<body>
<div class="page">
  <header>
    <div class="photo brand-photo" role="img" aria-label="Blue roadster with white stripes, front view"></div>
    <div class="abs brand-name"><span class="main">Kestrel Club</span><span class="sub">of New Zealand</span></div>
    <div class="abs ad-note">Please support our advertisers who fund this site for the benefit of all:</div>
    <div class="abs ad-box">Harbourline Motors</div>
  </header>

  <nav class="abs nav">
    <a style="width:90px">HOME</a>
    <a style="width:99px">EVENTS</a>
    <a style="width:98px">FORUM</a>
    <a style="width:104px">GALLERY</a>
    <a style="width:125px">MEMBERSHIP</a>
    <a style="width:127px">ADVERTISERS</a>
  </nav>

  <div class="photo" style="left:7px;top:189px;width:379px;height:206px;background:linear-gradient(#6f6a5e 0%,#a8a295 40%,#8c8d86 62%,#4d5a3f 80%,#2c2c2c 100%)" role="img" aria-label="Vintage propeller airliner on the tarmac under a stormy sky">
    <div class="caption">Kestrel's Take Flight - <span>View gallery »</span></div>
  </div>
  <div class="abs" style="left:400px;top:189px;width:270px">
    <h1 class="h-title">Welcome to Kestrel Club of New Zealand</h1>
    <div class="copy" style="position:static;margin-top:12px">
      <p>Our aim is to make this site user friendly and we have included a 'Forum' for the benefit of all Kestrel Roadster owners in New Zealand regardless of Kestrel kit type. Our intent for the Forum is to give those people interested/active in the Kestrel Roadster NZ scene a common vehicle to share ideas, problem solve and plan events.</p>
      <p>Our Calendar lists up-to-date and upcoming events. Check this regularly, especially for those last-minute runs that are often organised at very short notice upon the discovery of fine weather in Auckland!</p>
    </div>
  </div>

  <div class="h-box" style="left:7px;top:415px;width:323px">Members of all categories</div>
  <div class="copy" style="left:7px;top:459px;width:330px">
    <p>No matter where your taste lies, the Kestrel Club of New Zealand has members that fit all categories.</p>
    <p>From showing your prize possession off at a local car show or promotional event, to risking it all on the race track. If you're into Kestrels then this is the place to be!<br>The club regularly attends shows such as the Concours D'Elegance at Greenlane, All Marques Day and fundraising events such as the Prostate Cancer Runs. Just for that adrenalin rush a few hot laps at Waikato Raceway or even a tarmac rally, to test your nerves!</p>
    <p>So if you're into Kestrels, thinking of building one, looking for advice, or just need to be near one check out the Calendar pages or contact details</p>
  </div>
  <div class="photo" style="left:364px;top:417px;width:303px;height:201px;background:linear-gradient(160deg,#b9bcb8 0%,#6e7566 35%,#c7a830 60%,#3d3f38 100%)" role="img" aria-label="Yellow roadsters parked on grass at a concours show">
    <div class="caption">Greenlane Concours 2010 - <span>View gallery »</span></div>
  </div>

  <div class="h-box" style="left:7px;top:674px;width:323px">Kestrel Club of New Zealand History</div>
  <div class="copy" style="left:7px;top:718px;width:330px">
    <p>Grant H and Colin M started what is now the "Kestrel Club of New Zealand" in January 2002.</p>
    <p>The Club has since gone on to build the numbers by word of mouth, car rego searches, phone calls, articles, club listing in car magazines, car shows and now via our web page. Our membership has grown considerably since 2002 and we now have links with kestrel owners from the Far North to Southland.</p>
  </div>
  <div class="photo" style="left:400px;top:674px;width:267px;height:200px;background:linear-gradient(#dfe3ea 0%,#c4cad3 40%,#3c5ea8 65%,#4b4f55 100%)" role="img" aria-label="Blue trucks and roadsters gathered for a charity run">
    <div class="caption">Cancer Run Support - <span>View gallery »</span></div>
  </div>

  <div class="photo" style="left:7px;top:897px;width:323px;height:151px;background:linear-gradient(#9ea8a9 0%,#7f8c77 45%,#5c6653 65%,#42474c 100%)" role="img" aria-label="View over a car bonnet following a red roadster along a country road"></div>
  <div class="photo" style="left:345px;top:897px;width:323px;height:151px;background:linear-gradient(#d9dadd 0%,#b6b9bc 35%,#5d6066 55%,#7a8a6a 75%,#4c4f52 100%)" role="img" aria-label="Roadster on a race track in front of the grandstand">
    <div class="caption">Madness at Waikato Raceway - <span>View gallery »</span></div>
  </div>

  <div class="abs rule"></div>
  <p class="abs disclaimer">This is not an official website related to the manufacture of Kestrel Roadster cars but it is a website devoted to all those that share a passion for the Kestrel Roadster.</p>
  <p class="abs sponsor-note">This site is proudly Sponsored by</p>
  <div class="abs sponsor">Garage Palisade</div>
</div>
</body>
</html>
```